Custom Wordpress Theme - Original and Professional

We are a boutique IT consulting firm that provide small and medium business in Australia three different levels of IT service.
We are looking for a developer who will create a customised, original and professional wordpress theme. We are looking for the developer to create a professional, clean, clear and simple theme with a stylish layout, images and icons.
Our three services are: IT support | IT Services | IT Solutions and we would like to clearly differentiate the difference in each level of service in as few words as possible.
IT Support is the ad hock “call us, when you need us” service, that smaller business or those with minimal issues use.
IT service is the unlimited service, that business with existing (and well maintained) IT systems choose and is both flexible and scalable including no contracts or paperwork required.
IT solutions are the unlimited service that businesses that need new or updated infrastructure choose and it includes all the hardware, software and services with no contracts or any ongoing commitment.
The main page on the web site will attract the visitor to choose the right “service level” for their business and then we will have a dedicated page for each service and another page for a comparison (table) to compare all three services.
Lastly we will need a contact us page that has both office locations (Sydney and Melbourne), contact phone numbers and an email form.
Items we are focused on for this project are: 1. Images, 2.Icons 3. Layout.
In summary we are looking for a custom WordPress theme into a 6 page (Home, IT Support, IT Services, IT Solutions, Compare Service levels and Contact us) website. The design must include relevant images and icons and be clear, simple, professional and sleek.

Thank you for your time and creativity and I look forward to working with you!

Target Market(s)

Small and Medium businesses in Australia

Industry/Entity Type

Boutique

Requirements
Must have
• - 6 Pages layout: Home, IT support, IT services, IT Solutions, Compare service levels and Contact us
- Images, Layout and Icons.
- Clean, Clear, Simple, Elegant, Stylish.
Nice to have
• - Some text (if possible but not required).
Should not have
• - Complexity.
- Confusing layout.
- Generic non matching images and icons.

```html
<!DOCTYPE html>
<html lang="en">
<head>
<meta charset="utf-8">
<title>Corvane IT – Contact Us</title>
<link rel="stylesheet" href="https://fonts.googleapis.com/css2?family=Michroma&family=Russo+One&family=Fjalla+One&family=Abel&family=Arimo:wght@400;700&display=swap">
<style>
  :root{
    --blue:#0f5fb0;
    --blue-light:#1880cc;
    --blue-dark:#0a4f94;
    --ink:#353433;
    --text:#333333;
    --field:#ececec;
    --field-border:#c9c9c9;
    --footer:#353433;
    --footer-text:#d7d7d7;
    --icon-grey:#8d8d8d;
    --white:#ffffff;
  }
  *{margin:0;padding:0;box-sizing:border-box}
  html,body{width:1128px;height:1200px;overflow:hidden;background:var(--white)}
  body{position:relative;font-family:"Arimo",Arial,sans-serif;color:var(--text)}
  .abs{position:absolute}

  /* header */
  .brand{left:40px;top:24px;display:flex;align-items:center;gap:14px;font-family:"Michroma",sans-serif;font-size:38px;line-height:44px;color:var(--blue);letter-spacing:3px}
  .brand-mark{width:30px;height:30px;background:var(--blue)}
  .enquiry-label{right:21px;top:14px;font-family:"Abel",sans-serif;font-size:18px;color:var(--blue);letter-spacing:.5px}
  .header-phone{right:21px;top:40px;display:flex;align-items:center;gap:8px;font-family:"Abel",sans-serif;font-size:31px;color:var(--ink)}

  /* navigation */
  .main-nav{left:0;top:90px;width:1128px;height:52px;background:linear-gradient(var(--blue-light),var(--blue-dark));box-shadow:0 3px 3px rgba(0,0,0,.25)}
  .main-nav a{font-family:"Michroma",sans-serif;font-size:14.5px;color:var(--white);text-decoration:none;letter-spacing:1px;position:absolute;top:0;height:52px;line-height:52px}
  .main-nav a.active{background:var(--ink);padding:0 18px}
  .main-nav a.active::before{content:"";position:absolute;left:50%;top:0;margin-left:-9px;border-style:solid;border-color:var(--white) transparent transparent;border-width:9px 9px 0}

  .banner{left:0;top:147px;width:1128px;height:277px;background:linear-gradient(90deg,#2a2a2a 0%,#6a6a6a 30%,#3a2a1a 55%,#b8650e 78%,#e08a1c 100%)}

  /* contact block */
  .phone-badge{left:45px;top:459px}
  .page-title{left:280px;top:470px;font-family:"Russo One",sans-serif;font-size:43px;letter-spacing:1px;color:var(--ink)}
  .company-name{left:281px;top:540px;font-family:"Arimo",sans-serif;font-weight:700;font-size:21px;color:#444}
  .address{left:281px;top:572px;font-size:16px;line-height:20.5px;color:#333;font-style:normal}
  .map{left:279px;top:700px;width:303px;height:194px;background:linear-gradient(135deg,#efefec,#e4e3df 60%,#d5e2c6)}

  .contact-form{left:680px;top:542px;width:373px}
  .field{display:block;width:373px;height:37px;margin-bottom:4.5px;background:var(--field);border:1px solid var(--field-border);border-radius:6px;padding:0 14px;font-family:"Arimo",sans-serif;font-weight:700;font-size:14px;color:#444;line-height:35px}
  .field.message{height:162px;line-height:20px;padding-top:10px}
  .submit{position:absolute;left:274px;top:297px;width:97px;height:40px;background:#4a4a4a;color:var(--white);border:none;border-radius:7px;font-family:"Fjalla One",sans-serif;font-size:21px}

  /* footer */
  .site-footer{left:0;top:935px;width:1128px;height:265px;background:var(--footer);color:var(--footer-text)}
  .footer-heading{font-family:"Fjalla One",sans-serif;font-size:20px;letter-spacing:.5px;color:var(--white);position:absolute;top:36px}
  .footer-nav{left:36px;top:74px;list-style:none;font-size:14px;line-height:18.4px}
  .quote-icon{left:376px;top:77px}
  .testimonial-text{left:442px;top:80px;width:300px;font-size:14px;line-height:17.3px;color:#cfcfcf}
  .testimonial-author{left:375px;top:154px;font-size:16px;color:var(--white)}
  .social{left:867px;top:78px;display:flex;gap:10px}
  .social span{width:32px;height:32px;border-radius:50%;background:var(--icon-grey)}
  .newsletter-note{left:868px;top:125px;font-size:12.5px;line-height:15px;color:var(--white)}
  .email-field{left:866px;top:165px;width:212px;height:31px;border-radius:16px;background:var(--field);color:#333;font-size:12.5px;line-height:31px;padding-left:17px}
  .subscribe{left:870px;top:211px;font-weight:700;font-size:12.5px;color:var(--white)}
</style>
</head>
<body>

<header>
  <div class="abs brand"><span class="brand-mark"></span>CORVANE IT</div>
  <div class="abs enquiry-label">FOR SERVICES &amp; INQUIRIES</div>
  <div class="abs header-phone">
    <svg width="30" height="30" viewBox="0 0 30 30" aria-hidden="true">
      <circle cx="15" cy="15" r="13.5" fill="none" stroke="#353433" stroke-width="2"/>
      <path d="M10 8.5c1-.8 2-.6 2.6.4l1.2 2.2c.4.8.2 1.5-.5 2l-.8.6c.6 1.6 1.7 2.9 3.2 3.8l.7-.8c.6-.6 1.3-.7 2-.3l2.2 1.3c.9.6 1 1.6.2 2.5-1.4 1.5-3.4 1.6-5.3.4-3.3-2-5.7-5.3-6.2-8.5-.2-1.4.2-2.8.7-3.6z" fill="#353433"/>
    </svg>
    0-20-5550199
  </div>
</header>

<nav class="abs main-nav">
  <a href="#" style="left:34px">HOME</a>
  <a href="#" style="left:135px">IT SUPPORT</a>
  <a href="#" style="left:308px">IT SERVICES</a>
  <a href="#" style="left:482px">IT SOLUTIONS</a>
  <a href="#" style="left:675px">COMPARE IT SERVICE</a>
  <a href="#" class="active" style="left:940px">CONTACT US</a>
</nav>

<div class="abs banner" role="img" aria-label="Banner photo: a hand presenting an envelope icon beside a glowing orange world map"></div>

<main>
  <svg class="abs phone-badge" width="184" height="184" viewBox="0 0 184 184" aria-hidden="true">
    <circle cx="92" cy="92" r="92" fill="#0f5fb0"/>
    <path d="M52 36c6-5 12-4 15 2l10 19c3 6 1 11-4 14l-6 4c5 15 14 27 27 35l6-5c5-4 10-4 15 0l16 14c5 4 5 11 0 16-10 10-24 10-38 1-24-15-41-40-46-64-2-14 0-28 5-36z" fill="#fff"/>
    <path d="M122 104a14 14 0 0 1 10 12M126 94a26 26 0 0 1 17 22M130 84a38 38 0 0 1 24 32" fill="none" stroke="#fff" stroke-width="6" stroke-linecap="round"/>
  </svg>

  <h1 class="abs page-title">CONTACT US</h1>
  <h2 class="abs company-name">CORVANE IT COMPANY</h2>
  <address class="abs address">
    Sydney: 4820 Harbour Lane, Suite 12<br>
    Melbourne: 75 Garden Row, Level 3<br>
    Tel Sydney: 0-200-5550147<br>
    Tel Melbourne: 0-300-5550162<br>
    Fax: 0-200-5550148<br>
    hello@corvane.example
  </address>
  <div class="abs map" role="img" aria-label="Street map showing the office location"></div>

  <form class="abs contact-form">
    <div class="field">full name</div>
    <div class="field">contact number</div>
    <div class="field">subject</div>
    <div class="field message">message</div>
    <button type="button" class="submit">submit</button>
  </form>
</main>

<footer class="abs site-footer">
  <h3 class="footer-heading" style="left:35px">NAVIGATION</h3>
  <ul class="abs footer-nav">
    <li>Home</li>
    <li>IT support</li>
    <li>IT Services</li>
    <li>IT Solutions</li>
    <li>Compare IT Service</li>
    <li>Contact Us</li>
  </ul>

  <h3 class="footer-heading" style="left:373px">TESTIMONIAL</h3>
  <svg class="abs quote-icon" width="54" height="50" viewBox="0 0 54 50" aria-hidden="true">
    <ellipse cx="21" cy="18" rx="20" ry="16" fill="none" stroke="#bdbdbd" stroke-width="3"/>
    <path d="M8 30l-4 10 10-6" fill="#bdbdbd"/>
    <ellipse cx="37" cy="32" rx="16" ry="13" fill="#bdbdbd"/>
    <path d="M48 42l4 7-10-4z" fill="#bdbdbd"/>
    <text x="12" y="25" font-family="Arial" font-weight="700" font-size="18" fill="#bdbdbd">“</text>
    <text x="29" y="44" font-family="Arial" font-weight="700" font-size="18" fill="#353433">”</text>
  </svg>
  <p class="abs testimonial-text">At vero eos et accusamus et iusto odio dignissimos ducimus, qui blanditiis praesentium voluptatum deleniti atque corrupti, quos dolores et quas molestias excepturi sint.”</p>
  <p class="abs testimonial-author">- Dana Whitfield</p>

  <h3 class="footer-heading" style="left:871px">CONTACT US</h3>
  <div class="abs social" aria-label="Social links">
    <span></span><span></span><span></span><span></span><span></span>
  </div>
  <p class="abs newsletter-note">subscribe to our monthly newsletter<br>and get the best deals and discounts</p>
  <div class="abs email-field">enter email address</div>
  <div class="abs subscribe">➤&nbsp;&nbsp;subscribe now</div>
</footer>

</body>
</html>
```